Stitch Haven web site

I have been running an online business for 6 years.
www.stitchhaven.com.au I specialise in ribbons, buttons and unique craft materials. I sell online to individuals and shops with seperate retail and wholesale sites. The web page I'd like redesigned is my retail site.

It needs a clean, fresh look. I've recently had a new logo designed (thanks pixel guild!) and want the web site to incorporate the new design and colour scheme of black and white. (new logo attached as a file)

I no longer want the page with the large image www.stitchhaven.com.au I want to have the first page as the retail shop homepage.
http://www.stitchhaven.com.au/index.php so this page needs to have all the links

I want to the look to be fresh, modern and clear. It needs to be quick to load.

Notes from my IT guru: They need to know that the following tend to remain static with just the content section changing on each page; Header Left column (but different in the cart) right column (if required) footer
Updates

Thanks for your designs. 1/3 of my users use mobile devices so please take that into consideration. I would like the logo to be incorporated into the design and be a prominent feature (most have just used it as a tiny image in the top left corner. I would like it to be larger and more prominent.  thanks                                   

Thanks to all the designers who have submitted. Can you please add  'Boutique craft supplies' near the logo. That is my tag line. Thanks

Target Market(s)

Crafty females of all ages

Industry/Entity Type

Business

Requirements
Must have
• links to;
blog
gallery
chatterbook
snapboard
wholesale
space for an image which I change approx every 2 weeks
about Stitch Haven
contact
privacy policy
terms and conditions
newsletter sign up
shipping info
product search
Nice to have
• I am not sure if I want product images on the homepage? I have attached a few images.
Should not have
• not too much colour - I hate the green border I have now

```html
<!DOCTYPE html>
<html lang="en">
<head>
<meta charset="utf-8">
<title>Stitch Haven – Boutique craft supplies</title>
<link rel="stylesheet" href="https://fonts.googleapis.com/css2?family=PT+Sans:wght@400;700&family=PT+Sans+Narrow&family=Arimo:wght@400;700&display=swap">
<style>
:root{
  --page:#ececec;
  --navy:#06305e;
  --navy-dark:#04254a;
  --ink:#1a1a1a;
  --muted:#666;
  --red:#e0102f;
  --panel:#e4e4e4;
  --white:#fff;
  --footer:#06111f;
  --footer-bar:#000;
  --footer-text:#e8e8e8;
}
*{box-sizing:border-box;margin:0;padding:0}
html,body{width:980px;height:1200px;overflow:hidden}
body{background:var(--page);font-family:"Arimo",Arial,sans-serif;color:var(--ink);position:relative}
.abs{position:absolute}

/* header */
.brand{left:127px;top:38px;width:175px;text-align:center;font:700 40px/1.05 "PT Sans",sans-serif;color:var(--ink)}
.login{left:581px;top:18px;font:13px "PT Sans",sans-serif;display:flex;align-items:center;gap:5px}
.mini-cart{left:642px;top:12px;width:225px;height:29px;border:1px solid #c8c8c8;border-radius:3px;background:linear-gradient(#f7f7f7,#e6e6e6);display:flex;align-items:center;font:12px "PT Sans",sans-serif}
.mini-cart .icon{margin:0 16px 0 6px}
.mini-cart .label{margin-right:16px}
.mini-cart .sum{margin-right:22px}
.mini-cart .go{margin-left:auto;width:30px;height:100%;border-left:1px solid #c8c8c8;display:flex;align-items:center;justify-content:center}
.search{left:702px;top:102px;width:164px;height:21px;border:1px solid #b9b9b9;border-radius:3px;background:var(--white);display:flex}
.search span{flex:1;font-size:10px;color:#888;padding:4px 8px;letter-spacing:.3px}
.search i{width:20px;border-left:1px solid #b9b9b9;display:flex;align-items:center;justify-content:center}

/* nav */
.main-nav{left:111px;top:140px;width:758px;height:28px;background:var(--navy);display:flex;list-style:none}
.main-nav li{color:var(--white);font:700 11px/28px "PT Sans",sans-serif;text-transform:uppercase;border-right:1px solid #3a5a82;text-align:center}
.main-nav li:last-child{border-right:0}

/* left column */
.sidebar{left:111px;top:168px;width:159px;height:773px;background:#f4f4f4;border:1px solid #d6d6d6;border-top:0}
.products{left:118px;top:183px;width:141px;height:481px;background:linear-gradient(90deg,#e9e9e9,#f7f7f7 40%,#e6e6e6);border-radius:3px;box-shadow:0 0 2px #bbb}
.products h2{position:absolute;left:0;top:0;width:128px;height:34px;background:linear-gradient(#fafafa,#cfcfcf);font:700 17px/34px "PT Sans",sans-serif;padding-left:18px;box-shadow:1px 1px 2px #999;text-transform:uppercase}
.products ul{position:absolute;left:13px;top:37px;width:116px;list-style:none}
.products li{font-size:10.5px;line-height:18.6px;height:18.6px;border-bottom:1px dashed #bdbdbd;white-space:nowrap}
.products li::before{content:"→ ";font-size:11px}
.cart{left:122px;top:683px;width:135px;height:181px;background:#efefef;border:1px solid #d2d2d2;border-radius:3px}
.cart h2{height:31px;background:var(--navy-dark);color:var(--white);font:700 15px/31px "PT Sans",sans-serif;padding-left:13px;margin:-1px -1px 0}
.cart .empty{margin:9px 8px 0 9px;padding-bottom:5px;border-bottom:1px dashed #777;font-size:10px;display:flex;align-items:center;gap:4px}
.cart .row{display:flex;justify-content:space-between;align-items:center;margin:0 8px 0 9px;font-size:9.5px}
.cart .row b{color:var(--red);font-weight:400;font-size:14px}
.cart .btn{display:block;margin:14px auto 0;width:90px;height:21px;background:var(--navy-dark);color:var(--white);font-size:9.5px;line-height:21px;text-align:center}

/* main */
.content{left:270px;top:168px;width:599px;height:773px;background:#f8f8f8}
.banner{left:275px;top:172px;width:594px;height:321px;border:1px solid #cfcfcf;background:var(--white)}
.banner .photo{height:240px;background:radial-gradient(circle at 25% 40%,#a9283a 0,transparent 28%),radial-gradient(circle at 55% 55%,#b48a8f 0,transparent 30%),radial-gradient(circle at 80% 40%,#8fb55b 0,transparent 30%),#f1efef}
.banner .copy{text-align:center;font-family:"PT Sans",sans-serif;margin-top:12px}
.banner h1{color:var(--red);font-size:14px;font-weight:700;text-transform:uppercase}
.banner p{font-size:10px;font-weight:700;text-transform:uppercase;margin-top:2px}
.banner .rates{display:flex;justify-content:center;gap:42px;margin-top:3px}
.banner .rates em{font-style:normal;color:var(--red)}
.banner small{display:block;font-family:"Arimo",sans-serif;font-size:7.5px;margin-top:7px;font-style:italic}

.section-title{display:flex;align-items:center;gap:5px;font:700 16px "PT Sans",sans-serif}
.latest-title{left:287px;top:514px}
.latest-band{left:275px;top:505px;width:594px;height:200px;border-top:1px solid #e5e5e5;border-bottom:1px solid #e5e5e5}
.card{top:545px;width:126px;height:153px;background:var(--panel);border-radius:2px}
.card .thumb{margin:6px 6px 0;height:86px;border:1px solid #bbb;background:linear-gradient(90deg,#666 0 22%,#d66 22% 40%,#bdd98a 40% 57%,#e8d36e 57% 73%,#b9d7e0 73% 88%,#74bccf 88%)}
.card .name{font-size:8.5px;color:var(--muted);text-align:center;margin-top:4px}
.card .buy{display:flex;justify-content:space-between;align-items:center;margin:6px 6px 0 7px}
.card .price{color:var(--red);font:700 13px "PT Sans",sans-serif}
.card .btn{background:var(--navy-dark);color:var(--white);font:700 9px/18px "Arimo",sans-serif;padding:0 6px}

.popular-title{left:291px;top:740px}
.blog-title{left:584px;top:740px}
.popular{left:288px;top:769px;width:268px;height:153px;background:var(--panel)}
.popular ul{list-style:none;margin:16px 0 0 22px}
.popular li{color:var(--red);font-size:10px;font-weight:700;line-height:20.6px;display:flex;align-items:center;gap:8px}
.popular li::before{content:"";width:7px;height:7px;border-radius:50%;background:#999;box-shadow:inset 0 0 0 2px #ddd}
.blog{left:584px;top:769px;width:269px;height:153px;background:var(--panel);padding:10px 12px 0 14px}
.post{display:flex;gap:11px}
.post + .post{border-top:1px dashed #888;margin-top:9px;padding-top:11px}
.date{flex:none;width:46px;height:46px;border-radius:4px;background:var(--white);border:2px solid #6b1a14;text-align:center;overflow:hidden}
.date b{display:block;background:#c8261b;color:var(--white);font-size:7px;line-height:11px}
.date span{font:700 21px/31px "PT Sans",sans-serif}
.post h3{color:var(--red);font-size:10.5px}
.post p{font-size:9px;line-height:13px;margin-top:2px}
.post a{display:block;text-align:right;color:#a03070;font-size:7px;margin:2px 8px 0 0;text-decoration:none}

/* footer */
.footer{left:0;top:947px;width:980px;height:225px;background:var(--footer)}
.footer-rule{left:134px;top:989px;width:691px;height:1px;background:#333c48}
.foot-title{top:960px;font:400 19px/24px "PT Sans Narrow",sans-serif;color:var(--footer-text);white-space:nowrap}
.sitemap{left:136px;top:995px;list-style:none}
.sitemap li{color:var(--white);font:700 11px/18.6px "PT Sans",sans-serif}
.newsletter{left:374px;top:1011px;width:213px;height:21px;border:1px solid #8a8a8a;border-radius:3px;display:flex;overflow:hidden}
.newsletter span{flex:1;font-size:9.5px;color:#aaa;padding:4px 10px}
.newsletter b{width:55px;background:var(--white);color:#222;font:400 12px/19px "Arimo",sans-serif;text-align:center}
.badge-a{left:374px;top:1077px;width:119px;height:59px;background:linear-gradient(90deg,#5a4a40,#d8c9c4)}
.badge-b{left:496px;top:1106px;width:85px;height:29px;background:linear-gradient(90deg,#5a2d8f,#2a6fc8)}
.social{left:740px;display:flex;align-items:center;gap:4px;font:700 10px "PT Sans",sans-serif;color:var(--white)}
.social i{width:14px;height:14px;background:var(--white);display:block}
.foot-brand{left:718px;top:1092px;width:125px;text-align:center;font:700 20px/1.05 "PT Sans",sans-serif;color:var(--white)}
.copyright{left:0;top:1172px;width:980px;height:28px;background:var(--footer-bar);color:#aaa;font-size:7.5px;line-height:28px;text-align:center;letter-spacing:.4px}
</style>
</head>
<body>

<header>
  <div class="abs brand">Stitch<br>Haven</div>
  <div class="abs login">
    <svg width="10" height="12" viewBox="0 0 10 12"><path d="M2 5V3.5a3 3 0 0 1 6 0V5" fill="none" stroke="#555" stroke-width="1.4"/><rect x="0.5" y="5" width="9" height="6.5" rx="1" fill="#666"/></svg>
    Login
  </div>
  <div class="abs mini-cart">
    <svg class="icon" width="24" height="20" viewBox="0 0 24 20"><path d="M1 2h4l3 11h12l3-8H7" fill="none" stroke="#111" stroke-width="2"/><circle cx="10" cy="17" r="2" fill="#111"/><circle cx="18" cy="17" r="2" fill="#111"/></svg>
    <span class="label">My Cart</span><span class="sum">$00</span><span>0Items</span>
    <span class="go"><svg width="12" height="16" viewBox="0 0 12 16"><path d="M2 1l8 7-8 7" fill="none" stroke="#c8161b" stroke-width="3"/></svg></span>
  </div>
  <div class="abs search"><span>Enter key word..</span><i><svg width="10" height="10" viewBox="0 0 10 10"><circle cx="4" cy="4" r="3" fill="none" stroke="#555" stroke-width="1.3"/><path d="M6.3 6.3L9.5 9.5" stroke="#555" stroke-width="1.4"/></svg></i></div>
  <ul class="abs main-nav">
    <li style="width:76px">Home</li>
    <li style="width:145px">About Stitch Haven</li>
    <li style="width:87px">Gallery</li>
    <li style="width:107px">Wholesale</li>
    <li style="width:117px">Shipping Info</li>
    <li style="width:71px">Blog</li>
    <li style="width:155px">Contact Us</li>
  </ul>
</header>

<aside class="abs sidebar"></aside>
<nav class="abs products">
  <h2>Products</h2>
  <ul>
    <li>New Products</li><li>** Clearance **</li><li>Adhesives</li><li>Buttons</li><li>Card Kits</li><li>Charms</li><li>Chipboard</li><li>Christmas</li><li>Embellishments</li><li>Embossing Folders</li><li>Flowers and Leaves</li><li>Inks, Mists and Masks</li><li>Lace</li><li>Miscellaneous</li><li>Paper</li><li>Punches</li><li>Ribbon Club</li><li>Ribbons</li><li>Ribbons - organza</li><li>Ric Rac</li><li>Sequins</li><li>Stamps</li><li>Stickers</li><li>Washi tape</li>
  </ul>
</nav>
<section class="abs cart">
  <h2>Shopping Cart</h2>
  <div class="empty">Your basket is empty.
    <svg width="16" height="14" viewBox="0 0 24 20"><path d="M1 2h4l3 11h12l3-8H7" fill="none" stroke="#111" stroke-width="2.4"/><circle cx="10" cy="17" r="2" fill="#111"/><circle cx="18" cy="17" r="2" fill="#111"/></svg>
  </div>
  <div class="row" style="margin-top:10px">Items in cart: <b>0</b></div>
  <div class="row" style="margin-top:12px">Total: <b>$0.00</b></div>
  <span class="btn">View Basket</span>
</section>

<main>
  <div class="abs content"></div>
  <section class="abs banner">
    <div class="photo" role="img" aria-label="Organza ribbon flowers with beaded centres in red, pink and green"></div>
    <div class="copy">
      <h1>Lorem ipsum proin gravida nibh vel velit auctor aliquet</h1>
      <p>Postage rates (within Australia only)</p>
      <p class="rates"><span>Orders over $50 - <em>Free postage</em></span><span>Orders under $50 - <em>$6 postage charge</em></span></p>
      <small>NO international postage without prior postage price agreement. Please do not order online if you do not have an Australian address.</small>
    </div>
  </section>

  <div class="abs latest-band"></div>
  <h2 class="abs section-title latest-title">
    <svg width="34" height="22" viewBox="0 0 34 22"><g fill="#b5b5b5"><rect x="0" y="8" width="3" height="3"/><rect x="4" y="8" width="3" height="3"/><rect x="8" y="5" width="3" height="3"/><rect x="8" y="11" width="3" height="3"/></g><path d="M13 6h9V0l11 11-11 11v-6h-9z" fill="#a7a7a7"/></svg>
    Latest Products
  </h2>
  <article class="abs card" style="left:288px"><div class="thumb" role="img" aria-label="Rolls of washi tape"></div><p class="name">Washi tape - blue pattern</p><div class="buy"><span class="price">$3.50</span><span class="btn">Buy Now</span></div></article>
  <article class="abs card" style="left:433px"><div class="thumb" role="img" aria-label="Rolls of washi tape"></div><p class="name">Washi tape - blue pattern</p><div class="buy"><span class="price">$3.50</span><span class="btn">Buy Now</span></div></article>
  <article class="abs card" style="left:578px"><div class="thumb" role="img" aria-label="Rolls of washi tape"></div><p class="name">Washi tape - blue pattern</p><div class="buy"><span class="price">$3.50</span><span class="btn">Buy Now</span></div></article>
  <article class="abs card" style="left:724px"><div class="thumb" role="img" aria-label="Rolls of washi tape"></div><p class="name">Washi tape - blue pattern</p><div class="buy"><span class="price">$3.50</span><span class="btn">Buy Now</span></div></article>

  <h2 class="abs section-title popular-title">
    <svg width="34" height="22" viewBox="0 0 34 22"><g fill="#b5b5b5"><rect x="0" y="8" width="3" height="3"/><rect x="4" y="8" width="3" height="3"/><rect x="8" y="5" width="3" height="3"/><rect x="8" y="11" width="3" height="3"/></g><path d="M13 6h9V0l11 11-11 11v-6h-9z" fill="#a7a7a7"/></svg>
    Popular Products
  </h2>
  <section class="abs popular">
    <ul>
      <li>Lorem Ipsum Proin gravida nibh vel Proin</li>
      <li>Lorem Ipsum Proin gravida nibh vel Ipsum</li>
      <li>Lorem Ipsum Proin gravida nibh vel nibh</li>
      <li>Lorem Ipsum Proin gravida nibh vel</li>
      <li>Lorem Ipsum Proin gravida nibh vel gravida</li>
      <li>Lorem Ipsum Proin gravida nibh vel</li>
    </ul>
  </section>

  <h2 class="abs section-title blog-title">
    <svg width="34" height="22" viewBox="0 0 34 22"><g fill="#b5b5b5"><rect x="0" y="8" width="3" height="3"/><rect x="4" y="8" width="3" height="3"/><rect x="8" y="5" width="3" height="3"/><rect x="8" y="11" width="3" height="3"/></g><path d="M13 6h9V0l11 11-11 11v-6h-9z" fill="#a7a7a7"/></svg>
    Blog
  </h2>
  <section class="abs blog">
    <article class="post">
      <div class="date"><b>MAY</b><span>30</span></div>
      <div><h3>Lorem Ipsum Proin gravida nibh vel</h3><p>Lorem Ipsum. Proin gravida nibh vel velit auctor aliquet. Aenean sollicitudin..</p><a>Read more ➔</a></div>
    </article>
    <article class="post">
      <div class="date"><b>MAY</b><span>25</span></div>
      <div><h3>Lorem Ipsum Proin gravida nibh vel</h3><p>Lorem Ipsum. Proin gravida nibh vel velit auctor aliquet. Aenean sollicitudin..</p><a>Read more ➔</a></div>
    </article>
  </section>
</main>

<footer>
  <div class="abs footer"></div>
  <div class="abs footer-rule"></div>
  <h4 class="abs foot-title" style="left:134px">Sitemap</h4>
  <h4 class="abs foot-title" style="left:401px">Subscribe to our newsletter</h4>
  <h4 class="abs foot-title" style="left:739px">Letsget Social</h4>
  <ul class="abs sitemap">
    <li>Home</li><li>About Stitch Haven</li><li>Gallery</li><li>Wholesale</li><li>Shipping info</li><li>Blog</li><li>Contact us</li><li>Privacy Policy</li><li>Terms and Conditions</li>
  </ul>
  <div class="abs newsletter"><span>Enter your email address</span><b>Join</b></div>
  <div class="abs badge-a" role="img" aria-label="Craft listing badge"></div>
  <div class="abs badge-b" role="img" aria-label="Craft listing badge"></div>
  <div class="abs social" style="top:1005px"><i></i>chatterbook</div>
  <div class="abs social" style="top:1025px"><i></i>snapboard</div>
  <div class="abs foot-brand">Stitch<br>Haven</div>
  <div class="abs copyright">Copyright © 2013 Stitch Haven, All right reserved.</div>
</footer>

</body>
</html>
```